Website Design for Arena on Draft: Sports TV for bars and restaurants

We need a website design for a streaming service called Arena on Draft. Arena on Draft provides sports programming to bars and restaurants across the United States and Canada. We would like to see a design that uses the colors of red, black, gold, and white. The final design should be functional business site, designed primarily for registration and ordering capabilities. In addition to a Registration and an Order page, we would like to see the following pages: Upcoming Events, FAQs, and About. We would also like to see an option at the top of the page to switch between languages (English and Spanish)

Target Market(s)

Male, 21-45 years old

Industry/Entity Type

Sports Bar

Number of Pages Required

5+ page

Font styles to use
Serif
Sans Serif

Requirements
Must have
• The project must have an easy to use registration page that include the following fields: Establishment's Name, Manager's name and contact info (phone number and email), and a field to upload a picture of their fire code. The project also must have an easy to use Upcoming events page with the ability to upload a fight's promotional poster.
Nice to have
• Nice to have an area on the main home page for testimonials and a scrolling ticker to put our partner's logos.

```html
<!DOCTYPE html>
<html lang="en">
<head>
<meta charset="utf-8">
<title>Arena on Draft</title>
<link href="https://fonts.googleapis.com/css2?family=Bebas+Neue&family=Open+Sans:ital,wght@0,400;0,600;0,700;1,400&family=Syncopate:wght@700&display=swap" rel="stylesheet">
<style>
:root{
  --red:#cc0a1e;
  --red-dark:#a80716;
  --gold:#f2a900;
  --black:#161616;
  --ink:#222;
  --muted:#666;
  --line:#d9d9d9;
  --white:#fff;
}
*{margin:0;padding:0;box-sizing:border-box}
html,body{width:1200px;height:3982px;overflow:hidden;background:var(--white)}
body{position:relative;font-family:"Open Sans",sans-serif;color:var(--ink)}
.abs{position:absolute}
.btn{position:absolute;display:flex;align-items:center;justify-content:center;border-radius:30px;font-family:"Open Sans",sans-serif;font-weight:700;font-size:15px;text-transform:uppercase;letter-spacing:.5px}
.btn-gold{background:var(--gold);color:var(--white)}
.btn-outline{border:2px solid var(--gold);color:var(--gold);background:var(--white)}

/* nav */
.topbar{left:0;top:0;width:1200px;height:88px;background:var(--red);z-index:5}
.topbar a{position:absolute;top:30px;font-family:"Bebas Neue",sans-serif;font-size:27px;color:var(--white);text-decoration:none;letter-spacing:.5px}
.topbar a.active{color:var(--gold)}
.brand{position:absolute;left:0;width:1200px;text-align:center;top:24px;font-family:"Bebas Neue",sans-serif;font-size:40px;color:var(--white);letter-spacing:1px}
.search{position:absolute;left:1062px;top:34px}

/* hero */
.hero{left:0;top:0;width:1200px;height:830px}
.hero-title{left:0;top:300px;width:1200px;text-align:center;font-family:"Syncopate",sans-serif;font-weight:700;font-size:58px;letter-spacing:8px;color:var(--white)}
.hero-sub{left:230px;top:398px;width:740px;text-align:center;color:var(--white);font-size:21px;font-weight:600;line-height:36px}
.dots{left:567px;top:716px;display:flex;gap:6px}
.dots span{width:12px;height:12px;border-radius:50%;border:2px solid var(--white)}
.dots span.on{background:var(--white)}

/* welcome */
.section-title{left:0;width:1200px;text-align:center;font-family:"Bebas Neue",sans-serif;font-size:50px;color:var(--black);letter-spacing:.5px}
.welcome-text{left:175px;top:980px;width:850px;text-align:center;font-size:14px;line-height:27px;color:var(--muted)}

/* registration */
.reg-photo{left:98px;top:1261px;width:502px;height:425px;background:radial-gradient(circle at 60% 35%,#b06a5a 0%,#6a2a3c 35%,#2a1418 75%,#120a0c 100%)}
.play{left:318px;top:1440px}
.reg-panel{left:600px;top:1261px;width:502px;height:425px;background:var(--red)}
.reg-title{left:600px;top:1298px;width:502px;text-align:center;font-family:"Bebas Neue",sans-serif;font-size:54px;color:var(--white)}
.field{position:absolute;height:45px;background:var(--white);font-size:14px;color:#555;padding:0 12px;display:flex;align-items:center;justify-content:space-between}

/* testimonial */
.testimonial{left:0;top:1792px;width:1200px;height:518px;background:linear-gradient(100deg,#141820 0%,#2a2a30 35%,#6b5040 60%,#c08a50 80%,#8a6a48 100%)}
.quote-mark{left:98px;top:1872px}
.quote-text{left:98px;top:1992px;width:470px;font-style:italic;font-size:15px;line-height:30px;color:var(--white)}
.quote-name{left:98px;top:2190px;font-size:16px;font-weight:700;color:var(--white)}
.arrow-btn{position:absolute;width:48px;height:48px;border-radius:50%;background:var(--white);display:flex;align-items:center;justify-content:center}

/* events */
.event-card{left:98px;top:2496px;width:438px;height:500px;background:var(--white);border:1px solid #e4e4e4;box-shadow:0 2px 10px rgba(0,0,0,.12)}
.event-card-photo{left:104px;top:2502px;width:426px;height:234px;background:linear-gradient(180deg,#26324a 0%,#3c5a6a 40%,#3f7a3a 70%,#2f5e28 100%)}
.event-heading{font-family:"Bebas Neue",sans-serif;color:var(--black);position:absolute}
.meta{position:absolute;font-size:12px;color:#555;display:flex;align-items:center;gap:6px}
.meta i{display:inline-block;width:10px;height:10px;background:var(--red);border-radius:1px}
.excerpt{position:absolute;font-size:13px;line-height:21px;color:#555}
.read-more{left:130px;top:2952px;font-size:13px;font-weight:700;color:var(--gold);text-transform:uppercase}
.thumb{position:absolute;left:568px;width:138px;height:112px;border:4px solid var(--white);box-shadow:0 1px 6px rgba(0,0,0,.2)}
.divider{left:98px;top:3088px;width:1004px;height:2px;background:var(--line)}

/* partners */
.partners-glow{left:0;top:3240px;width:1200px;height:220px;background:radial-gradient(ellipse at center,#fff8e0 0%,rgba(255,255,255,0) 70%)}
.partner{position:absolute;background:var(--white);border:2px solid #cfcfcf;display:flex;align-items:center;justify-content:center}
.partner span{display:block;width:60%;height:30px;background:#bdbdbd;border-radius:4px}
.partner.featured{border-color:#bdbdbd;box-shadow:0 3px 12px rgba(0,0,0,.15)}
.partner.featured span{background:#3a9a4a;height:40px}

/* footer */
.footer-shape{left:0;top:3490px}
.footer-brand{left:150px;top:3740px;width:210px;text-align:center;font-family:"Bebas Neue",sans-serif;font-size:44px;line-height:46px;color:var(--white)}
.footer-head{position:absolute;top:3678px;font-family:"Bebas Neue",sans-serif;font-size:26px;color:var(--white)}
.footer-links{left:425px;top:3722px;list-style:none;font-size:12px;line-height:25px;color:#ddd}
.news-text{left:605px;top:3722px;width:270px;font-size:12px;line-height:20px;color:#ddd}
.news-input{left:605px;top:3775px;width:253px;height:35px;background:var(--white);font-size:12px;color:#777;padding:0 10px;display:flex;align-items:center}
.contact-row{position:absolute;left:935px;display:flex;gap:22px;font-size:12px;line-height:19px;color:#ddd}
.contact-row svg{flex:none;margin-top:3px}
.copyright{left:98px;top:3924px;font-size:12px;color:#ccc}
.socials{left:984px;top:3918px;display:flex;gap:8px}
.socials span{width:22px;height:22px;border-radius:50%;border:1px solid #bbb}
</style>
</head>
<body>

<!-- hero -->
<svg class="abs hero" width="1200" height="830" viewBox="0 0 1200 830" role="img" aria-label="Friends cheering and watching a game on screens in a sports bar">
  <defs>
    <linearGradient id="heroFill" x1="0" y1="0" x2="1" y2="1">
      <stop offset="0" stop-color="#2c2a2a"/>
      <stop offset=".45" stop-color="#4a3a30"/>
      <stop offset=".75" stop-color="#3a2a22"/>
      <stop offset="1" stop-color="#1a1412"/>
    </linearGradient>
  </defs>
  <path d="M0 0H1200V612C1060 690 720 740 600 826C480 740 140 690 0 612Z" fill="var(--gold)"/>
  <path d="M0 0H1200V600C1060 678 720 728 600 812C480 728 140 678 0 600Z" fill="url(#heroFill)"/>
</svg>

<header class="abs topbar">
  <a class="active" style="left:120px">Home</a>
  <a style="left:204px">About</a>
  <a style="left:292px">Upcoming Events</a>
  <div class="brand">ARENA ON DRAFT</div>
  <a style="left:746px">Register</a>
  <a style="left:860px">FAQ</a>
  <a style="left:929px">Contact Us</a>
  <svg class="search" width="20" height="20" viewBox="0 0 20 20"><circle cx="8" cy="8" r="6" fill="none" stroke="#fff" stroke-width="3"/><line x1="12.5" y1="12.5" x2="18" y2="18" stroke="#fff" stroke-width="3"/></svg>
</header>

<h1 class="abs hero-title">ARENA ON DRAFT</h1>
<p class="abs hero-sub">Arena on Draft provides sports programming to bars and restaurants across the United States and Canada.</p>
<div class="btn btn-gold" style="left:504px;top:500px;width:191px;height:57px">Explore More</div>
<div class="abs dots"><span class="on"></span><span></span><span></span><span></span></div>

<!-- welcome -->
<h2 class="abs section-title" style="top:895px">Welcome to Arena on Draft</h2>
<p class="abs welcome-text">Nemo enim ipsam voluptatem quia voluptas sit aspernatur aut odit aut fugit, sed quia consequuntur magni dolores eos qui ratione voluptatem sequi nesciunt. Neque porro quisquam est, qui dolorem ipsum quia dolor sit amet, consectetur, adipisci velit, sed quia non numquam eius modi tempora incidunt ut labore et dolore magnam aliquam quaerat voluptatem. Ut enim ad minima veniam, quis nostrum exercitationem ullam corporis suscipit laboriosam.</p>
<div class="btn btn-outline" style="left:523px;top:1133px;width:157px;height:57px">About Us</div>

<!-- quick registration -->
<div class="abs reg-photo" role="img" aria-label="Video still of friends celebrating at a bar counter"></div>
<svg class="abs play" width="66" height="66" viewBox="0 0 66 66"><circle cx="33" cy="33" r="31" fill="#111" stroke="#fff" stroke-width="3"/><path d="M26 20L47 33L26 46Z" fill="#fff"/></svg>
<section class="abs reg-panel"></section>
<h2 class="abs reg-title">Quick Registration</h2>
<div class="field" style="left:619px;top:1388px;width:225px">Establishment's Name</div>
<div class="field" style="left:855px;top:1388px;width:226px">Manager's name</div>
<div class="field" style="left:619px;top:1447px;width:225px">Phone Number</div>
<div class="field" style="left:855px;top:1447px;width:226px">Email</div>
<div class="field" style="left:619px;top:1505px;width:462px">Upload a Picture
  <svg width="16" height="16" viewBox="0 0 16 16"><path d="M8 2L3 7H6V11H10V7H13Z" fill="#777"/><rect x="2" y="12" width="12" height="2" fill="#777"/></svg>
</div>
<div class="btn btn-gold" style="left:778px;top:1580px;width:143px;height:58px">Submit</div>

<!-- testimonial -->
<section class="abs testimonial" role="img" aria-label="Sprinter crossing the finish line in a stadium at sunset"></section>
<svg class="abs quote-mark" width="96" height="80" viewBox="0 0 96 80"><path d="M0 80V40C0 18 10 4 34 0V14C22 18 18 26 18 36H40V80ZM54 80V40C54 18 64 4 88 0V14C76 18 72 26 72 36H94V80Z" fill="var(--gold)"/></svg>
<p class="abs quote-text">Nemo enim ipsam voluptatem quia voluptas sit aspernatur aut odit aut fugit, sed quia consequuntur magni dolores eos qui ratione voluptatem sequi nesciunt. Neque porro quisquam est, qui dolorem ipsum quia dolor sit amet, consectetur, adipisci velit, sed quia non numquam eius modi tempora incidunt ut</p>
<p class="abs quote-name">- MARCUS DELGADO</p>
<div class="arrow-btn" style="left:356px;top:2175px"><svg width="12" height="18" viewBox="0 0 12 18"><path d="M10 2L3 9L10 16" fill="none" stroke="#333" stroke-width="2.5"/></svg></div>
<div class="arrow-btn" style="left:418px;top:2175px"><svg width="12" height="18" viewBox="0 0 12 18"><path d="M2 2L9 9L2 16" fill="none" stroke="#333" stroke-width="2.5"/></svg></div>

<!-- upcoming events -->
<h2 class="abs section-title" style="top:2392px">Upcoming Events</h2>
<article class="abs event-card"></article>
<div class="abs event-card-photo" role="img" aria-label="Football players tackling on a floodlit pitch"></div>
<h3 class="event-heading" style="left:130px;top:2760px;font-size:32px">Finibus Bonorum et Malorum</h3>
<div class="meta" style="left:130px;top:2806px"><i></i>28/12/2017 &nbsp;|&nbsp; <i></i>John Doe</div>
<p class="excerpt" style="left:130px;top:2838px;width:380px">Nam libero tempore, cum soluta nobis est eligendi optio cumque nihil impedit quo minus id quod maxime placat facere possimus, omnis voluptas voluptatibus maioresalis consequ expedita distinct.</p>
<p class="abs read-more">Read More</p>

<div class="thumb" style="top:2496px;background:linear-gradient(135deg,#5a4a3a,#8a6a4a 50%,#3a3028)" role="img" aria-label="Crowd watching a match at a bar"></div>
<h3 class="event-heading" style="left:741px;top:2484px;font-size:27px">At vero eos et accusamus et iui</h3>
<div class="meta" style="left:741px;top:2524px"><i></i>28/12/2017 &nbsp;|&nbsp; <i></i>John Doe</div>
<p class="excerpt" style="left:741px;top:2550px;width:370px">Nam libero tempore, cum soluta nobis est eligendi optio cumque nihil impedit..</p>

<div class="thumb" style="top:2639px;background:linear-gradient(135deg,#8a8a8a,#c8c8c8 50%,#7a2a2a)" role="img" aria-label="Race cars on a track"></div>
<h3 class="event-heading" style="left:741px;top:2627px;font-size:27px">At vero eos et accusamus et iui</h3>
<div class="meta" style="left:741px;top:2667px"><i></i>28/12/2017 &nbsp;|&nbsp; <i></i>John Doe</div>
<p class="excerpt" style="left:741px;top:2693px;width:370px">Nam libero tempore, cum soluta nobis est eligendi optio cumque nihil impedit..</p>

<div class="thumb" style="top:2783px;background:linear-gradient(135deg,#2a4a6a,#6a7a5a 50%,#c8a040)" role="img" aria-label="Fans cheering in a bar"></div>
<h3 class="event-heading" style="left:741px;top:2771px;font-size:27px">At vero eos et accusamus et iui</h3>
<div class="meta" style="left:741px;top:2811px"><i></i>28/12/2017 &nbsp;|&nbsp; <i></i>John Doe</div>
<p class="excerpt" style="left:741px;top:2837px;width:370px">Nam libero tempore, cum soluta nobis est eligendi optio cumque nihil impedit..</p>

<div class="btn btn-gold" style="left:568px;top:2931px;width:138px;height:48px;font-size:13px">View All</div>
<div class="abs divider"></div>

<!-- partners -->
<div class="abs partners-glow"></div>
<h2 class="abs section-title" style="top:3165px">Our Partners</h2>
<svg class="abs" style="left:54px;top:3326px" width="14" height="22" viewBox="0 0 14 22"><path d="M12 2L3 11L12 20" fill="none" stroke="#888" stroke-width="2.5"/></svg>
<div class="partner" style="left:98px;top:3292px;width:186px;height:93px"><span></span></div>
<div class="partner" style="left:303px;top:3292px;width:170px;height:93px"><span></span></div>
<div class="partner featured" style="left:486px;top:3279px;width:228px;height:120px"><span></span></div>
<div class="partner" style="left:727px;top:3292px;width:170px;height:93px"><span></span></div>
<div class="partner" style="left:916px;top:3292px;width:186px;height:93px"><span></span></div>
<svg class="abs" style="left:1130px;top:3326px" width="14" height="22" viewBox="0 0 14 22"><path d="M2 2L11 11L2 20" fill="none" stroke="#888" stroke-width="2.5"/></svg>

<!-- footer -->
<svg class="abs footer-shape" width="1200" height="492" viewBox="0 0 1200 492">
  <path d="M0 172Q300 95 560 22Q600 10 640 22Q900 95 1200 172V492H0Z" fill="var(--black)"/>
  <path d="M0 166Q300 89 560 16Q600 4 640 16Q900 89 1200 166" fill="none" stroke="var(--red)" stroke-width="8"/>
</svg>
<div class="abs footer-brand">ARENA<br>ON DRAFT</div>

<h4 class="footer-head" style="left:425px">Quick Links</h4>
<ul class="abs footer-links">
  <li>Help</li><li>FAQ</li><li>Support</li><li>Sitemap</li><li>Terms Of Use</li><li>Privacy Statement</li>
</ul>

<h4 class="footer-head" style="left:605px">Newsletter Subscription</h4>
<p class="abs news-text">Register your Email Address to get information about us</p>
<div class="abs news-input">Email Address</div>
<div class="btn btn-gold" style="left:605px;top:3829px;width:104px;height:34px;font-size:12px">Subscribe</div>

<h4 class="footer-head" style="left:935px">Contact Us</h4>
<div class="contact-row" style="top:3725px">
  <svg width="12" height="16" viewBox="0 0 12 16"><path d="M6 0C2.7 0 0 2.6 0 6C0 10 6 16 6 16S12 10 12 6C12 2.6 9.3 0 6 0Z" fill="#ddd"/><circle cx="6" cy="6" r="2" fill="#161616"/></svg>
  <span>Lindenweg 14<br>4100 Aarfeld Switzerland</span>
</div>
<div class="contact-row" style="top:3782px">
  <svg width="14" height="14" viewBox="0 0 14 14"><path d="M3 0L5 4L3.5 5.5C4.5 7.5 6.5 9.5 8.5 10.5L10 9L14 11L13 14C6 14 0 8 0 1Z" fill="#ddd"/></svg>
  <span>1 800 555 0142</span>
</div>
<div class="contact-row" style="top:3822px">
  <svg width="14" height="11" viewBox="0 0 14 11"><rect width="14" height="11" fill="#ddd"/><path d="M0 0L7 6L14 0" fill="none" stroke="#161616" stroke-width="1.5"/></svg>
  <span>info@arenaondraft.com</span>
</div>

<p class="abs copyright">Copyrights © 2018, Arena on Draft. All rights reserved.</p>
<div class="abs socials"><span></span><span></span><span></span><span></span></div>

</body>
</html>
```